Investment company seeks website design

TBW (Tallowbrook Wealth Partners) are an investment company that actively targets and acquires businesses and grows them after acquisition.

The website design needs to be professional and should communicate to key decision-makers inside the acquirable companies that TBW targets.

You will design the Homepage initially for the competition. If you win the competition, you will design the inner pages too.

More details are attached below.

Target Market(s)

Business owners and decision makers inside acquirable companies

Industry/Entity Type

Company Investment

Number of Pages Required

5+ page

Requirements
Must have
• High Attention to Detail. Following the Wireframes closely. Consistent colour and design choices
Should not have
• Anything cheap, too bright or untidy

```html
<!DOCTYPE html>
<html lang="en">
<head>
<meta charset="utf-8">
<title>Tallowbrook Wealth Partners</title>
<link href="https://fonts.googleapis.com/css2?family=Montserrat:wght@400;500;600;700;800;900&display=swap" rel="stylesheet">
<style>
:root{
  --navy:#1f2e5c;
  --navy-deep:#14204a;
  --green:#6cab3c;
  --green-btn:#76b343;
  --green-dark:#3f7a1c;
  --text:#4a4f5c;
  --muted:#7b808c;
  --rule:#d4d7de;
  --white:#ffffff;
}
*{box-sizing:border-box;margin:0;padding:0}
html,body{width:1200px;height:4850px;overflow:hidden;background:var(--white)}
body{font-family:'Montserrat',sans-serif;color:var(--text);position:relative}
section,header,footer{position:absolute;left:0;width:1200px}
.hex{clip-path:polygon(50% 0,100% 25%,100% 75%,50% 100%,0 75%,0 25%)}
.btn{position:absolute;display:flex;align-items:center;justify-content:center;background:var(--green-btn);color:var(--white);font-size:14px;font-weight:500;letter-spacing:.3px}
.section-title{position:absolute;left:0;width:1200px;text-align:center;font-size:38px;font-weight:600;color:var(--navy)}
.section-title .accent{color:var(--green)}

/* header */
.site-header{top:0;height:90px;background:var(--white)}
.brand{position:absolute;left:111px;top:26px;display:flex;align-items:center;gap:12px;font-size:21px;font-weight:600;color:var(--navy)}
.brand-mark{width:26px;height:26px;background:var(--navy)}
.email-btn{left:968px;top:0;width:121px;height:38px;font-size:14px}
.main-nav a{position:absolute;top:56px;font-size:15px;color:var(--navy);text-decoration:none}

/* hero */
.hero{top:90px;height:585px;overflow:hidden}
.hero-photo{position:absolute;inset:0;background:linear-gradient(180deg,#7f8f8a 0%,#a3b59a 45%,#7fa35a 80%,#5f8a3b 100%)}
.hero-line{position:absolute;left:0;top:455px;width:1200px;height:3px;background:#1b2a22;opacity:.6}
.hero-text{position:absolute;line-height:1;white-space:nowrap}
.hero-small{color:var(--navy-deep);font-weight:800}
.hero-big{color:var(--green);font-weight:900}
.hero-mid{color:var(--navy-deep);font-weight:500}
.hero-btn{left:514px;top:485px;width:172px;height:38px}

/* thrive */
.thrive{top:675px;height:645px}
.thrive h2{position:absolute;left:111px;top:92px;font-size:40px;font-weight:600;line-height:48px;color:var(--navy)}
.thrive h2 span{color:var(--green)}
.thrive-intro{position:absolute;left:111px;top:194px;width:480px;font-size:14px;line-height:24px}
.services-label{position:absolute;left:111px;top:312px;font-size:16px;font-weight:700;color:var(--navy)}
.service-list{position:absolute;left:111px;top:350px;list-style:none}
.service-list li{display:flex;align-items:center;gap:10px;height:34px;font-size:14px}
.tick{width:16px;height:16px;flex:none}
.outline-btn{position:absolute;left:111px;top:531px;width:268px;height:42px;border:1.5px solid var(--navy);display:flex;align-items:center;justify-content:center;font-size:14.5px;font-weight:500;color:var(--navy);letter-spacing:.4px}
.thrive-photo{position:absolute;left:637px;top:75px;width:450px;height:516px;background:linear-gradient(135deg,#2b3d75 0%,#4c6a9c 40%,#8fb44b 70%,#b9cf3c 100%)}

/* qualities */
.qualities{top:1320px;height:728px}
.qualities .section-title{top:62px}
.core-photo{position:absolute;left:454px;top:202px;width:290px;height:333px;background:linear-gradient(160deg,#cfd3d8 0%,#b9c8c0 45%,#8db566 100%)}
.icon-hex{position:absolute;width:98px;height:112px;background:var(--navy);display:flex;align-items:center;justify-content:center}
.icon-hex .dot{width:34px;height:34px;border-radius:50%;border:3px solid var(--green)}
.quality{position:absolute}
.quality h3{font-size:22px;font-weight:600;color:var(--navy);line-height:28px}
.quality .bar{width:48px;height:2px;background:var(--green);margin:10px 0 10px}
.quality ul{list-style:none}
.quality li{font-size:13px;line-height:17px;margin-bottom:6px;display:flex;gap:8px}
.quality li .tick{width:13px;height:13px;margin-top:2px}
.quality.right-aligned{text-align:right}
.quality.right-aligned .bar{margin-left:auto}
.quality.right-aligned li{justify-content:flex-end}

/* explore */
.explore{top:2048px;height:386px;overflow:hidden}
.explore-photo{position:absolute;inset:0;background:linear-gradient(180deg,#1d2f74 0%,#243c8c 55%,#2a2f6e 100%)}
.explore h2{position:absolute;top:95px;width:1200px;text-align:center;font-size:38px;font-weight:600;color:var(--green)}
.explore p{position:absolute;top:156px;left:360px;width:480px;text-align:center;font-size:15px;line-height:27px;color:var(--white)}
.explore .btn{left:505px;top:254px;width:190px;height:40px}

/* transform */
.transform{top:2434px;height:656px}
.transform .section-title{top:118px;line-height:48px}
.step{position:absolute;top:250px;width:300px;text-align:center}
.step h3{font-size:22px;font-weight:500;color:var(--navy);line-height:32px}
.step-hex{position:absolute;top:320px;width:226px;height:256px;display:flex;align-items:flex-start;justify-content:center;padding:56px 30px 0;text-align:center;font-size:15px;font-weight:500;line-height:23px;color:var(--navy)}
.step-hex.sky{background:linear-gradient(180deg,#5fc7ef 0%,#9bd9f2 100%)}
.step-hex.sand{background:#ecd9c2}
.step-hex.mist{background:#f2efe9}

/* news */
.news{top:3090px;height:650px}
.news .section-title{top:50px}
.news-card{position:absolute;top:101px;width:310px}
.news-photo{height:194px;background:linear-gradient(135deg,#6e7370,#b9bdb5)}
.news-meta{margin-top:26px;font-size:12px;color:var(--muted)}
.news-card h3{margin-top:10px;font-size:21.5px;font-weight:500;line-height:29px;color:var(--navy)}
.news-card p{margin-top:14px;font-size:12.5px;line-height:25px;color:var(--muted)}
.news-card .more{display:inline-block;margin-top:10px;font-size:13px;font-weight:600;color:var(--navy);text-decoration:underline}

/* mosaic */
.mosaic{top:3740px;height:640px}
.tile{position:absolute;overflow:hidden}
.tile .label{position:absolute;bottom:28px;width:100%;text-align:center;font-size:29px;font-weight:600;color:var(--white);letter-spacing:.5px}
.mosaic-center{left:340px;top:0;width:520px;height:640px;background:linear-gradient(180deg,#1c1d22 0%,#3a3b3f 60%,#55575a 100%)}
.mosaic-center h2{position:absolute;top:40px;width:100%;text-align:center;font-size:29px;font-weight:600;line-height:48px;color:var(--white)}

/* footer */
.site-footer{top:4380px;height:470px}
.footer-col{position:absolute;top:98px}
.footer-col h4{font-size:17px;font-weight:700;color:var(--green-dark)}
.footer-col .rule{width:172px;height:2px;background:var(--navy);margin:12px 0 20px}
.footer-col a{display:block;font-size:13.5px;color:var(--navy);text-decoration:none;line-height:38px}
.contact-row{display:flex;gap:16px;align-items:flex-start;margin-bottom:18px;font-size:14px;line-height:26px;color:var(--navy)}
.contact-row svg{flex:none;margin-top:2px}
.footer-brand{position:absolute;left:791px;top:268px;display:flex;align-items:center;gap:14px;font-size:21px;font-weight:600;color:var(--navy);white-space:nowrap}
.footer-rule{position:absolute;left:111px;top:398px;width:978px;height:1px;background:var(--rule)}
.copyright{position:absolute;left:111px;top:422px;font-size:13px;color:var(--muted)}
.legal{position:absolute;right:111px;top:422px;font-size:13px;color:var(--muted)}
.legal span{margin:0 8px}
</style>
</head>
<body>

<svg width="0" height="0" style="position:absolute">
  <defs>
    <symbol id="tick" viewBox="0 0 16 16"><circle cx="8" cy="8" r="8" fill="#6cab3c"/><path d="M4.5 8.2l2.3 2.3 4.7-4.8" fill="none" stroke="#fff" stroke-width="1.8" stroke-linecap="round" stroke-linejoin="round"/></symbol>
  </defs>
</svg>

<header class="site-header">
  <div class="brand"><span class="brand-mark"></span>Tallowbrook Wealth Partners</div>
  <div class="btn email-btn">Email Us &nbsp;✉</div>
  <nav class="main-nav">
    <a style="left:543px">Our Approach</a>
    <a style="left:695px">Investment Criteria</a>
    <a style="left:887px">About Us</a>
    <a style="left:1000px">Contact Us</a>
  </nav>
</header>

<section class="hero">
  <div class="hero-photo" role="img" aria-label="Businessman balancing on a tightrope high above a city skyline under a cloudy sky"></div>
  <div class="hero-line"></div>
  <div class="hero-text hero-small" style="left:111px;top:216px;font-size:38px">The Best Exit</div>
  <div class="hero-text hero-big" style="left:109px;top:274px;font-size:92px">For You</div>
  <div class="hero-text hero-mid" style="left:665px;top:264px;font-size:40px">The Best Future for</div>
  <div class="hero-text hero-big" style="left:682px;top:310px;font-size:72px">Your</div>
  <div class="hero-text hero-big" style="left:693px;top:398px;font-size:72px">Business</div>
  <div class="btn hero-btn">DISCOVER TBW</div>
</section>

<section class="thrive">
  <h2>We Will Make<br><span>Your Business Thrive</span></h2>
  <p class="thrive-intro">TBW is committed to helping businesses achieve significant growth. Under our stewardship, companies have the benefit of an experienced team expert in operations and financing to ensure that every company achieves their full potential.</p>
  <div class="services-label">Our services include:</div>
  <ul class="service-list">
    <li><svg class="tick"><use href="#tick"/></svg>Crafting long-term growth</li>
    <li><svg class="tick"><use href="#tick"/></svg>Streamlining operations for maximum efficiency</li>
    <li><svg class="tick"><use href="#tick"/></svg>Providing expert advice to improve management decisions</li>
    <li><svg class="tick"><use href="#tick"/></svg>Optimizing financial structures for expansion</li>
    <li><svg class="tick"><use href="#tick"/></svg>Facilitating strategic mergers and acquisitions</li>
  </ul>
  <div class="outline-btn">UNLOCK YOUR POTENTIAL</div>
  <div class="thrive-photo hex" role="img" aria-label="Business handshake and hands holding a young green plant, framed in a hexagon"></div>
</section>

<section class="qualities">
  <h2 class="section-title">Our Qualities <span class="accent">&amp; Capabilities</span></h2>
  <div class="core-photo hex" role="img" aria-label="Desk with business charts and documents in a hexagon frame"></div>
  <div class="icon-hex hex" style="left:398px;top:159px"><span class="dot"></span></div>
  <div class="icon-hex hex" style="left:697px;top:159px"><span class="dot"></span></div>
  <div class="icon-hex hex" style="left:403px;top:466px"><span class="dot"></span></div>
  <div class="icon-hex hex" style="left:697px;top:466px"><span class="dot"></span></div>

  <div class="quality right-aligned" style="right:787px;top:254px;width:300px">
    <h3>Driving Value</h3><div class="bar"></div>
    <ul>
      <li><svg class="tick"><use href="#tick"/></svg>Comprehensive long-term plan</li>
      <li><svg class="tick"><use href="#tick"/></svg>Ownership of company performance</li>
      <li><svg class="tick"><use href="#tick"/></svg>Vast experience in driving<br>transformation</li>
    </ul>
  </div>
  <div class="quality" style="left:786px;top:254px;width:260px">
    <h3>Integrated Team</h3><div class="bar"></div>
    <ul>
      <li><svg class="tick"><use href="#tick"/></svg>Partnership Culture</li>
      <li><svg class="tick"><use href="#tick"/></svg>Consistent senior team</li>
      <li><svg class="tick"><use href="#tick"/></svg>Detailed industry and operating<br>experience</li>
    </ul>
  </div>
  <div class="quality right-aligned" style="right:808px;top:430px;width:300px">
    <h3>Partnership<br>with Management</h3><div class="bar"></div>
    <ul>
      <li><svg class="tick"><use href="#tick"/></svg>Strong, trust-based relationships</li>
      <li><svg class="tick"><use href="#tick"/></svg>Significant commitment of time<br>on-the-ground</li>
      <li><svg class="tick"><use href="#tick"/></svg>Ability to take interim roles if needed</li>
    </ul>
  </div>
  <div class="quality" style="left:806px;top:458px;width:260px">
    <h3>Accelerated Execution</h3><div class="bar"></div>
    <ul>
      <li><svg class="tick"><use href="#tick"/></svg>Relentless focus on priorities.</li>
      <li><svg class="tick"><use href="#tick"/></svg>Drive through to results</li>
      <li><svg class="tick"><use href="#tick"/></svg>Committed to continuous<br>development</li>
    </ul>
  </div>
</section>

<section class="explore">
  <div class="explore-photo" role="img" aria-label="Businessman stepping forward on a path, tinted deep blue"></div>
  <h2>Explore Your Next Move</h2>
  <p>If you are looking for a change, then TBW can help you map out a smooth transition, and give you the confidence that your company is in safe hands.</p>
  <div class="btn">DISCUSS WITH TBW</div>
</section>

<section class="transform">
  <h2 class="section-title">How TBW Will<br><span class="accent">Transform Your Company</span></h2>
  <div class="step" style="left:87px"><h3>Discover Growth<br>Opportunities</h3></div>
  <div class="step" style="left:449px"><h3>Craft Strategic<br>Solutions</h3></div>
  <div class="step" style="left:813px"><h3>Drive Future<br>Success</h3></div>
  <div class="step-hex hex sky" style="left:124px" role="img" aria-label="Illustration of a person beside a flowing ribbon of growth">Identify hidden growth opportunities for your business</div>
  <div class="step-hex hex sand" style="left:486px" role="img" aria-label="Illustration of a person planning strategy with icons">Develop precise, results-driven strategies to drive your company forward</div>
  <div class="step-hex hex mist" style="left:850px" role="img" aria-label="Illustration of a rising bar chart with a flag on top">Lead your company through trans-formative processes to achieve tangible success</div>
</section>

<section class="news">
  <h2 class="section-title">TBW <span class="accent">News &amp; Insights</span></h2>
  <article class="news-card" style="left:111px">
    <div class="news-photo" role="img" aria-label="Hand watering a potted plant shaped like a rising arrow"></div>
    <div class="news-meta">By TBW 05 April 2024</div>
    <h3>Lorem ipsum is placeholder text commonly the graphic,</h3>
    <p>Lorem ipsum dolor sit amet, consectetur adipiscing elit, sed do eiusmod tempor incid-idunt ut labore et dolore magna aliqua.</p>
    <a class="more">Read More</a>
  </article>
  <article class="news-card" style="left:445px">
    <div class="news-photo" style="background:linear-gradient(135deg,#8a6a4c,#d8c7b0)" role="img" aria-label="Calm office worker meditating amid flying papers"></div>
    <div class="news-meta">By TBW 05 April 2024</div>
    <h3>Lorem ipsum is placeholder text commonly the graphic,</h3>
    <p>Lorem ipsum dolor sit amet, consectetur adipiscing elit, sed do eiusmod tempor incid-idunt ut labore et dolore magna aliqua.</p>
    <a class="more">Read More</a>
  </article>
  <article class="news-card" style="left:779px">
    <div class="news-photo" style="background:linear-gradient(135deg,#2f4a78,#c3cfdc)" role="img" aria-label="Financial charts on paper and tablet during a review meeting"></div>
    <div class="news-meta">By TBW 05 April 2024</div>
    <h3>Lorem ipsum is placeholder text commonly the graphic,</h3>
    <p>Lorem ipsum dolor sit amet, consectetur adipiscing elit, sed do eiusmod tempor incid-idunt ut labore et dolore magna aliqua.</p>
    <a class="more">Read More</a>
  </article>
</section>

<section class="mosaic">
  <div class="tile" style="left:0;top:0;width:340px;height:320px;background:linear-gradient(135deg,#0f3550,#2a6f8f 50%,#b0553a)" role="img" aria-label="Digital world map with financial data overlay"><div class="label">FINANCE</div></div>
  <div class="tile" style="left:0;top:320px;width:340px;height:320px;background:linear-gradient(135deg,#2a2b2e,#6b6d70)" role="img" aria-label="Two businessmen shaking hands"><div class="label">PARTNERSHIPS</div></div>
  <div class="tile mosaic-center" role="img" aria-label="Hand watering a potted plant shaped like a rising arrow"><h2>Tallowbrook Wealth Partners:<br>Providing Balance and Growth<br>to Your Business</h2></div>
  <div class="tile" style="left:860px;top:0;width:340px;height:320px;background:linear-gradient(135deg,#d9c6ae,#b8712e)" role="img" aria-label="Hands joining two jigsaw puzzle pieces"><div class="label">STRATEGY</div></div>
  <div class="tile" style="left:860px;top:320px;width:340px;height:320px;background:linear-gradient(135deg,#5a3d2c,#a7896d)" role="img" aria-label="Business team discussing work around a board"><div class="label">OPERATIONS</div></div>
</section>

<footer class="site-footer">
  <div class="footer-col" style="left:111px">
    <h4>Quick Links</h4><div class="rule"></div>
    <a>Our Approach</a><a>Investment Criteria</a><a>About Us</a><a>Contact Us</a>
  </div>
  <div class="footer-col" style="left:409px">
    <h4>Our Team</h4><div class="rule"></div>
    <div class="contact-row">
      <svg width="40" height="40" viewBox="0 0 40 40"><rect width="40" height="40" rx="8" fill="#3f7a1c"/><path d="M14 11c1 0 2 3 2 4s-2 2-2 2c1 3 4 6 7 7 0 0 1-2 2-2s4 1 4 2-2 5-4 5C16 29 11 21 11 15c0-2 2-4 3-4z" fill="#fff"/></svg>
      <div>Call toll free:<br>+44 (0) 7700 900318</div>
    </div>
    <div class="contact-row">
      <svg width="40" height="40" viewBox="0 0 40 40"><rect width="40" height="40" rx="8" fill="#3f7a1c"/><rect x="10" y="13" width="20" height="14" rx="2" fill="#fff"/><path d="M10 14l10 7 10-7" fill="none" stroke="#3f7a1c" stroke-width="2"/></svg>
      <div>Email:<br>hello@tallowbrook.example</div>
    </div>
  </div>
  <div class="footer-col" style="left:748px">
    <h4>Address</h4><div class="rule"></div>
    <div class="contact-row" style="font-weight:500">
      <svg width="40" height="40" viewBox="0 0 40 40"><path d="M20 4c-7 0-12 5-12 12 0 9 12 21 12 21s12-12 12-21c0-7-5-12-12-12z" fill="#3f7a1c"/><circle cx="20" cy="16" r="5" fill="#fff"/></svg>
      <div style="line-height:30px">Tallowbrook Wealth Partners Ltd.<br>Harbourline Business Centre Marlow Row<br>Port Ellery Westhaven</div>
    </div>
  </div>
  <div class="footer-brand"><span class="brand-mark" style="width:30px;height:30px"></span>Tallowbrook Wealth Partners</div>
  <div class="footer-rule"></div>
  <div class="copyright">2024 (c) Tallowbrook Wealth Partners.</div>
  <div class="legal">Sitemap<span>|</span>Terms of Use<span>|</span>Privacy Policy<span>|</span>Contact Us</div>
</footer>

</body>
</html>
```